Quillavet Shampoo

Quillavet shampoo is aimed to be a "novelty" item, with an intriguing mix of ingredients including but not limited to CBD & caffeine. We want a design that has a unique way of portraying "quillavet". Get creative with this one. We want the designers to get creative and think outside of the box, and maybe even get a little crazy (but not too crazy), because that's what the premise of the shampoo is; out of the box thinking -- "quillavet". Try to incorporate what you think of when you hear the word quillavet.

On the front of the bottle is where the main design will be shown. On the back will be the ingredients list, and will have a bit more information. The design should flow well with a darkish-brown bottle, pictured in the attachments called "bottle-size-template".

Avoid simple designs. We want our shampoo to stand out, not stand on the shelves. Get creative. IMPORTANT NOTE: Please do not use / inspire from the attachments called "bottle-size-template", as these are to show you what the bottle looks like, and what the label will look like on the bottle. DO NOT MAKE YOUR DESIGN BASED FROM THOSE ATTACHMENTS!

If you are feeling like a winner, you can even insert the correct ingredients list: Purified water (aqua), pure virgin hemp seed oil, green tea essential oil, green tea extract, aloe vera, ginseng extract, cam-phor essential oil, glycerin(vegetable), borage seed oil, lauryl glucoside, coconut oil, yucca extract, dermochlorella extract(seaweed based), nettle extract, coco glucoside, jojoba oil, awapuhi, soluble natural plant collagen, wheat germ glycerides (gluten free), echinacea extract, licorice root extract, cocoa butter, ivy extract, soy protein non-GMO), ascorbyl tetraisopalmitate (palm based), golden seal extract, behenic acid (natural based) guar gum, ylang ylang extract, sea salt.

```html
<!DOCTYPE html>
<html lang="en">
<head>
<meta charset="utf-8">
<title>Quillavet Shampoo – Label</title>
<link rel="stylesheet" href="https://fonts.googleapis.com/css2?family=PT+Sans:wght@400;700&family=PT+Sans+Narrow:wght@400;700&display=swap">
<style>
  :root {
    --backdrop: #e6e7e8;
    --label: #ffffff;
    --ink: #2a2a2a;
    --navy: #1e3d6b;
    --bar-start: #4a4a4a;
    --bar-end: #9a9a9a;
    --brain-tint: #dde6f1;
    --brain-edge: #b9cbe0;
  }
  * { box-sizing: border-box; margin: 0; padding: 0; }
  html, body {
    width: 1054px; height: 1200px; overflow: hidden;
    background: var(--backdrop);
  }
  .canvas { position: relative; width: 1054px; height: 1200px; }
  .label-panel {
    position: absolute; top: 315px; width: 500px; height: 570px;
    background: var(--label); overflow: hidden;
  }
  .label-back { left: 17px; }
  .label-front { left: 537px; }

  .brain-art {
    position: absolute; top: 30px; width: 230px; height: 500px;
    background: var(--brain-tint);
    border: 3px solid var(--brain-edge);
    border-radius: 50%;
  }
  .label-back .brain-art { left: 385px; }
  .label-front .brain-art { left: -115px; }

  /* back panel */
  .back-copy {
    position: absolute; left: 18px; font-family: "PT Sans Narrow", sans-serif;
    font-size: 11.5px; line-height: 1.5; color: var(--ink); text-align: justify;
  }
  .intro-copy { top: 48px; width: 336px; }
  .section-bar {
    position: absolute; left: 18px; height: 15px;
    background: linear-gradient(90deg, var(--bar-start), var(--bar-end));
    color: #fff; font-family: "PT Sans", sans-serif; font-size: 10.5px;
    letter-spacing: 1px; text-align: center; line-height: 15px;
  }
  .ingredients-bar { top: 156px; width: 336px; }
  .ingredients-copy { top: 176px; width: 336px; }
  .direction-bar { top: 343px; width: 230px; }
  .direction-copy { top: 362px; width: 230px; }

  /* front panel */
  .front-stack {
    position: absolute; left: 150px; width: 340px; top: 0;
    text-align: center; color: var(--navy);
  }
  .range-name {
    position: absolute; top: 66px; width: 100%;
    font-family: "PT Sans Narrow", sans-serif; font-size: 50px; font-weight: 400;
    line-height: 1; color: #111; letter-spacing: 0.5px;
  }
  .product-name {
    position: absolute; top: 168px; width: 100%;
    font-family: "PT Sans", sans-serif; font-size: 68px; font-weight: 400;
    line-height: 1; color: var(--navy);
  }
  .product-type {
    position: absolute; top: 302px; width: 100%;
    font-family: "PT Sans Narrow", sans-serif; font-size: 28px; line-height: 1.5;
  }
  .divider {
    position: absolute; top: 398px; left: 64px; width: 212px; height: 2px;
    background: var(--navy);
  }
  .product-size {
    position: absolute; top: 422px; width: 100%;
    font-family: "PT Sans Narrow", sans-serif; font-size: 28px; line-height: 1.45;
    color: #222;
  }
</style>
</head>
<body>
<main class="canvas">
  <section class="label-panel label-back">
    <p class="back-copy intro-copy">Lorem ipsum dolor sit amet, consectetuer adipiscing elit, sed diam nonummy nibh euismod tincidunt ut laoreet dolore magna aliquam erat volutpat. Ut wisi enim ad minim veniam, quis nostrud exerci tation ullamcorper suscipit lobortis nisl ut aliquip ex ea commodo consequat. Duis autem vel eum iriure dolor in hendrerit in vulputate velit esse molestie consequat, vel illum dolore eu feugiat.</p>
    <div class="section-bar ingredients-bar">INGREDIENTS LIST:</div>
    <p class="back-copy ingredients-copy">Purified water (aqua), pure virgin hemp seed oil, green tea essential oil, green tea extract, aloe vera, ginseng extract, cam-phor essential oil, glycerin(vegetable), borage seed oil, lauryl glucoside, coconut oil, yucca extract, dermochlorella extract (seaweed based), nettle extract, coco glucoside, jojoba oil, awapuhi, soluble natural plant collagen, wheat germ glycerides (gluten free), echinacea extract, licorice root extract, cocoa butter, ivy extract, soy protein non-GMO), ascorbyl tetraisopalmitate (palm based), golden seal extract, behenic acid (natural based) guar gum, ylang ylang extract, sea salt.</p>
    <div class="section-bar direction-bar">DIRECTION</div>
    <p class="back-copy direction-copy">Lorem ipsum dolor sit amet, consectetuer adipiscing elit, sed diam nonummy nibh euismod tincidunt ut laoreet aliquam erat volutpat.</p>
    <div class="brain-art" role="img" aria-label="Right half of a blue line drawing of a brain seen from above"></div>
  </section>

  <section class="label-panel label-front">
    <div class="brain-art" role="img" aria-label="Left half of a blue line drawing of a brain seen from above"></div>
    <div class="front-stack">
      <p class="range-name">MERIVANE</p>
      <h1 class="product-name">quillavet</h1>
      <p class="product-type">Hair Shampoo<br>Strengthnes Weak Hair</p>
      <div class="divider"></div>
      <p class="product-size">For All Hair Types<br>500ml/17.7 fl.oz</p>
    </div>
  </section>
</main>
</body>
</html>
```